Healthcare recruitment agency - Brochure Design Project

We are looking to develop a new brochure for our business. Rather than a brochure we will actually have 4 x A4 double sided flyers.
Each flyer will have the same content on front side and sector specific content on the back page.
The sectors will be:
a. Homelessness & Substance Misuse
b. Elderly Care
c. Learning Disabilities
d. Mental Health
It is important for us to get the base design right as this will follow suit across all our communications, the winning designer will get more work including mouse mat, folder and further flyers.
We are a people orientated business for both our staff and the people who they care for, imagery is important and we will source the final images (a couple attached to start things rolling).
I also like the idea of a people montage (see eye montage for an idea of what i mean) This could help describe the varied healthcare element of what we do and extend to other marketing materials with the relevant image highlighted from the rest.
Initially focus on 1 x double sided A4 flyer so we can get the design right, then we can go from there! Also attached is some copy to add to the initial flyer to help the concept develop.
Once the base design has been agreed, images and copy will be sent for the other x3 flyers to make up the equivalent of an 8pp brochure, although x4 pages will be identical.
The first page is generic about the company
The second page is on 'homeless and substance misuse' support staff.
Update: I have just added a file (vonel logo) this is the group logo that should be on the front page somewhere. Plus a AI version of the Pexar logo.
Updates
Hi Guys,
Target Market(s)
Healthcare and social care market, care managers, senior healthcare buyers
Industry/Entity Type
Healthcare
Requirements
Must have
- Our logo and group logo
Use our colours of green, grey and plum (in that order)

```html
<!DOCTYPE html>
<html lang="en">
<head>
<meta charset="utf-8">
<title>Pexar Healthcare Talent – Flyer Cover</title>
<link rel="stylesheet" href="https://fonts.googleapis.com/css2?family=Questrial&display=swap">
<style>
  :root {
    --brand-green: #9bb555;
    --brand-plum: #a3317f;
    --stage: #d6d6d6;
    --paper: #ffffff;
    --montage-light: #f6f5f5;
    --montage-mid: #e7e4e3;
    --photo-light: #a49f99;
    --photo-mid: #6a625c;
    --photo-dark: #34302d;
    --group-panel: rgba(255, 255, 255, 0.86);
    --ink: #2b2a2e;
  }
  html, body {
    margin: 0;
    padding: 0;
    width: 698px;
    height: 1200px;
    overflow: hidden;
    background: var(--stage);
    font-family: "Questrial", "Century Gothic", sans-serif;
  }
  .canvas {
    position: relative;
    width: 698px;
    height: 1200px;
  }
  .flyer {
    position: absolute;
    left: 29px;
    top: 147px;
    width: 640px;
    height: 905px;
    background: var(--paper);
    box-shadow: 0 6px 24px rgba(0, 0, 0, 0.18);
  }
  .flyer-art {
    display: block;
    width: 100%;
    height: 100%;
  }
  .brand-name,
  .brand-tagline,
  .group-name {
    font-family: "Questrial", "Century Gothic", sans-serif;
    fill: var(--ink);
  }
</style>
</head>
<body>
<main class="canvas">
  <article class="flyer">
    <svg class="flyer-art" viewBox="0 0 475 672" preserveAspectRatio="none" xmlns="http://www.w3.org/2000/svg">
      <defs>
        <linearGradient id="montage-tone" x1="0" y1="0" x2="0" y2="1">
          <stop offset="0" stop-color="var(--montage-mid)"/>
          <stop offset="1" stop-color="var(--montage-light)"/>
        </linearGradient>
        <linearGradient id="photo-tone" x1="0.8" y1="0" x2="0.2" y2="1">
          <stop offset="0" stop-color="var(--photo-light)"/>
          <stop offset="0.55" stop-color="var(--photo-mid)"/>
          <stop offset="1" stop-color="var(--photo-dark)"/>
        </linearGradient>
      </defs>

      <rect class="people-montage" x="0" y="0" width="475" height="672" fill="url(#montage-tone)" role="img" aria-label="Faint montage of many small portrait photos of people"/>

      <path class="hero-photo" d="M0,425 Q155,240 475,208 L475,672 L0,672 Z" fill="url(#photo-tone)" role="img" aria-label="Photo of a person lying on the pavement beneath a railing, representing homelessness support"/>

      <path class="swoosh-green" d="M0,338 Q140,225 475,198 L475,203 Q150,235 0,385 Z" fill="var(--brand-green)"/>
      <path class="swoosh-plum" d="M0,385 Q150,235 475,203 L475,208 Q155,240 0,425 Z" fill="var(--brand-plum)"/>

      <text class="brand-name" x="237" y="118" font-size="44" text-anchor="middle">Pexar</text>
      <text class="brand-tagline" x="237" y="146" font-size="15" text-anchor="middle">Healthcare Talent</text>

      <rect class="group-panel" x="302" y="513" width="143" height="159" fill="var(--group-panel)"/>
      <circle class="group-mark" cx="334" cy="580" r="5" fill="var(--ink)"/>
      <text class="group-name" x="345" y="589" font-size="26">vonel</text>
    </svg>
  </article>
</main>
</body>
</html>
```